Brightgate Homes is a company designed to assist distressed homeowners short sell their property

Brightgate Homes is a company designed to assist distressed homeowners liquidate their real properties for less than is owed on their mortgage. We help consumers through a stressful and difficult period of time by becoming their liaisons and advocates. We work with mortgage lenders to negotiate a reduced payoff amount that will satisfy all parties involved including the buyer, seller, and junior lien holders.

Target Market(s)

Distressed homeowner, Real estate Brokers & Agents

Industry/Entity Type

Real Estate

Coding

Coded - Design and coding required

Number of Pages Required

3 page

Font styles to use
Sans Serif

Requirements
Must have
• Small, simple, and elegant header. Must have a large photo under the header that fits within the screen, without having to scroll down to view the entire image. It should include a few simple words on the cover photo with a call to action, that does not cover the intended image or placed on the side. Under the large photo, we would like to have the ability to add additional content that can be a preview to other pages. This content would be viewed by scrolling down. We would like colors that work well with our logo. We are also requesting that the design be coded and fully developed in WordPress. Our current domain is purchased, brightgatehomes.example and will be hosted by NetHarbor.
Nice to have
• Example website: https://www.pixelmarsh.example/photos/about/?page=home or http://www.quillvane.example/ or https://www.tovaro.example/. We like to have the picture on the first page have some sort of action, such as zooming in to the picture.
Should not have
• Should not have too many variant colors. Should not feel too busy. No pop-ups.

```html
<!DOCTYPE html>
<html lang="en">
<head>
<meta charset="utf-8">
<title>Brightgate Homes</title>
<link href="https://fonts.googleapis.com/css2?family=Open+Sans:wght@400;600;700&display=swap" rel="stylesheet">
<style>
:root{
  --orange:#e8621e;
  --black:#111111;
  --dark:#2b2b2b;
  --panel:#3a3a3a;
  --field:#4a4a4a;
  --grey-bg:#f2f2f2;
  --text:#333333;
  --muted:#8a8a8a;
  --white:#ffffff;
}
*{margin:0;padding:0;box-sizing:border-box}
html,body{width:1200px;height:2656px;overflow:hidden}
body{font-family:"Open Sans",Arial,sans-serif;color:var(--text);background:var(--white)}
a{color:inherit;text-decoration:none}

.site-header{height:112px;background:var(--black);display:flex;align-items:center;justify-content:space-between;padding:0 40px}
.brand{display:flex;align-items:center;gap:14px;color:var(--white);font-weight:700;font-size:30px}
.brand-mark{width:30px;height:30px;background:var(--orange)}
.main-nav{display:flex;gap:44px;font-size:15px;color:#cfcfcf}
.main-nav .active{color:var(--orange)}

.hero{position:relative;height:528px;background:linear-gradient(180deg,#c9dcee 0%,#e9eef2 45%,#b9b1a4 100%);overflow:hidden}
.hero-photo{position:absolute;inset:0}
.hero-copy{position:absolute;right:110px;top:60px;width:340px;text-align:right}
.hero-copy h1{font-size:42px;font-weight:700;color:var(--text);margin-bottom:14px;line-height:1.3}
.hero-copy p{font-size:15px;line-height:1.5;color:#444;margin-bottom:26px}
.btn{display:inline-block;background:var(--orange);color:var(--white);font-weight:700;font-size:15px;padding:18px 30px;border-radius:2px}
.hero-copy .btn{background:#f5a300;color:var(--text)}
.slider-arrow{position:absolute;top:244px;width:40px;height:40px;border-radius:50%;background:rgba(0,0,0,.35)}
.slider-arrow.prev{left:24px}.slider-arrow.next{right:24px}
.slider-arrow svg{display:block;margin:10px}

.section-title{text-align:center;font-size:26px;font-weight:700;text-transform:uppercase;color:var(--text)}
.section-sub{text-align:center;font-size:17px;color:var(--muted);margin-top:6px}

.services{height:400px;padding-top:40px}
.service-grid{display:grid;grid-template-columns:repeat(4,1fr);width:1000px;margin:64px auto 0;text-align:center}
.service svg{display:block;margin:0 auto 22px}
.service h3{font-size:16px;font-weight:700;text-transform:uppercase;margin-bottom:12px}
.service p{font-size:13px;line-height:1.6;color:var(--muted);width:190px;margin:0 auto}

.about{height:400px;background:var(--grey-bg);position:relative}
.about-photo{position:absolute;left:170px;top:84px;width:232px;height:232px;border-radius:50%;border:6px solid var(--white);background:linear-gradient(160deg,#dfe6ee,#8aa8c8 60%,#f2f2f2)}
.about-text{position:absolute;left:450px;top:110px;width:680px}
.about-text .kicker{font-size:22px;color:var(--muted)}
.about-text h2{font-size:24px;font-weight:700;text-transform:uppercase;line-height:1.1}
.about-text .rule{width:80px;height:3px;background:var(--orange);margin:18px 0 22px}
.about-text p{font-size:13px;line-height:1.8;color:var(--muted)}

.blog{height:420px;padding-top:48px}
.post-grid{display:flex;gap:40px;width:1000px;margin:44px auto 0}
.post{display:flex;gap:20px;width:480px;align-items:flex-start}
.post-img{position:relative;width:216px;height:188px;flex:none}
.post-img.one{background:linear-gradient(180deg,#a9c6e2 0%,#c9a58a 55%,#6f8d4e 100%)}
.post-img.two{background:linear-gradient(180deg,#b8d0e6 0%,#e4dccb 55%,#7f9e5a 100%)}
.tag{position:absolute;top:10px;right:0;background:var(--orange);color:var(--white);font-size:10px;padding:3px 8px}
.post-img.two .tag{background:var(--dark)}
.post h3{font-size:20px;font-weight:700;line-height:1.2;margin-bottom:8px}
.post .meta{font-size:11px;color:var(--muted);margin-bottom:10px}
.post p{font-size:12px;line-height:1.7;color:var(--muted);margin-bottom:10px}
.post .more{font-size:12px;color:var(--orange);font-weight:600}

.connect{height:588px;background:var(--dark);display:flex;gap:100px;padding:48px 100px 0}
.connect-col{width:450px}
.connect-head{text-align:center;color:var(--white);margin-bottom:24px}
.connect-head .small{font-size:20px;color:#aaa}
.connect-head .big{font-size:24px;font-weight:700;text-transform:uppercase;line-height:1.1}
.testimonial{background:var(--orange);height:424px;text-align:center;color:var(--white);padding:52px 50px 0}
.avatar{width:80px;height:80px;border-radius:50%;background:#f3c6a8;margin:0 auto 16px}
.testimonial h4{font-size:18px;font-weight:700}
.testimonial .role{font-size:11px;opacity:.85;margin-bottom:26px}
.testimonial blockquote{font-size:13px;line-height:1.8}
.dots{display:flex;gap:8px;justify-content:center;margin-top:40px}
.dots span{width:10px;height:10px;border-radius:50%;background:rgba(255,255,255,.5)}
.dots span.on{background:var(--white)}
.contact-form{background:var(--panel);height:424px;padding:40px 40px 0}
.row{display:flex;gap:16px;margin-bottom:16px}
.field{flex:1;height:38px;background:var(--field);color:#aaa;font-size:12px;padding:11px 12px}
.field.msg{height:140px}
.contact-form .btn{float:right;font-size:12px;padding:10px 22px;margin-top:4px}

.site-footer{height:208px;background:var(--black);color:#bbb;text-align:center;padding-top:40px;position:relative}
.foot-nav{display:flex;justify-content:center;gap:50px;font-size:13px;padding-bottom:20px;border-bottom:1px solid #333;width:700px;margin:0 auto}
.foot-nav .active{color:var(--white)}
.social{display:flex;gap:18px;justify-content:center;margin:22px 0 18px}
.social span{width:14px;height:14px;border-radius:50%;background:#bbb}
.copy{font-size:12px}
.to-top{position:absolute;right:30px;bottom:26px;font-size:11px;color:#888}
</style>
</head>
<body>

<header class="site-header">
  <a class="brand" href="#"><span class="brand-mark"></span>Brightgate Homes</a>
  <nav class="main-nav">
    <a class="active" href="#">Home</a><a href="#">About Us</a><a href="#">Services</a><a href="#">Properties</a><a href="#">Advice</a><a href="#">Blog</a><a href="#">Contact Us</a>
  </nav>
</header>

<section class="hero">
  <div class="hero-photo" role="img" aria-label="Couple standing in front of a large white two-storey house"></div>
  <div class="hero-copy">
    <h1>Brightgate Homes</h1>
    <p>We help distressed homeowners liquidate their real properties for less than it is owed on their mortgage</p>
    <a class="btn" href="#">GET STARTED NOW</a>
  </div>
  <span class="slider-arrow prev"><svg width="20" height="20" viewBox="0 0 20 20"><path d="M13 3 6 10l7 7" fill="none" stroke="#fff" stroke-width="2.5"/></svg></span>
  <span class="slider-arrow next"><svg width="20" height="20" viewBox="0 0 20 20"><path d="M7 3l7 7-7 7" fill="none" stroke="#fff" stroke-width="2.5"/></svg></span>
</section>

<section class="services">
  <h2 class="section-title">Our Services</h2>
  <p class="section-sub">Integer vitae libero ac risus egestas placerat</p>
  <div class="service-grid">
    <div class="service">
      <svg width="56" height="56" viewBox="0 0 56 56" fill="none" stroke="#e8621e" stroke-width="2.5"><circle cx="22" cy="18" r="9"/><path d="M6 48c0-10 7-16 16-16s16 6 16 16"/><circle cx="40" cy="22" r="7"/><path d="M40 34c6 0 11 5 11 13"/></svg>
      <h3>Lorem Ipsum</h3>
      <p>Simple guidance from the first call to closing, with clear steps for owners.</p>
    </div>
    <div class="service">
      <svg width="56" height="56" viewBox="0 0 56 56" fill="none" stroke="#e8621e" stroke-width="2.5"><path d="M14 6h20l10 10v34H14z"/><path d="M34 6v10h10M20 26h18M20 33h18M20 40h12"/></svg>
      <h3>Dolor Sit Amet</h3>
      <p>We prepare every lender file and keep each document current and complete.</p>
    </div>
    <div class="service">
      <svg width="56" height="56" viewBox="0 0 56 56" fill="none" stroke="#e8621e" stroke-width="2.5"><rect x="8" y="12" width="40" height="36" rx="2"/><path d="M8 22h40M18 6v10M38 6v10"/><path d="M16 30h6M25 30h6M34 30h6M16 38h6M25 38h6"/></svg>
      <h3>Contaney Popular</h3>
      <p>Fast scheduling that fits your timeline and keeps the sale moving forward.</p>
    </div>
    <div class="service">
      <svg width="56" height="56" viewBox="0 0 56 56" fill="none" stroke="#e8621e" stroke-width="2.5"><circle cx="28" cy="28" r="8"/><path d="M28 6v8M28 42v8M6 28h8M42 28h8M12 12l6 6M38 38l6 6M44 12l-6 6M18 38l-6 6"/></svg>
      <h3>Popular Sit</h3>
      <p>Agents and brokers get steady support on every short sale they list.</p>
    </div>
  </div>
</section>

<section class="about">
  <div class="about-photo" role="img" aria-label="Smiling team of real estate advisors"></div>
  <div class="about-text">
    <p class="kicker">Lorem ipsum dolor sit</p>
    <h2>About Us</h2>
    <div class="rule"></div>
    <p>We act as liaisons and advocates for homeowners facing a hard season. Our team works with mortgage lenders to negotiate a reduced payoff that satisfies every party involved, including the buyer, the seller and junior lien holders. From the first review to the final signature we stay beside you, explain each step and keep the process calm and clear.</p>
  </div>
</section>

<section class="blog">
  <h2 class="section-title">Latest Blog</h2>
  <p class="section-sub">Integer vitae libero ac risus egestas placerat</p>
  <div class="post-grid">
    <article class="post">
      <div class="post-img one" role="img" aria-label="Row of brick townhouses"><span class="tag">Advice</span></div>
      <div>
        <h3>Lorem ipsum dolor sit amet contanty</h3>
        <p class="meta">Admin · 3 Comments</p>
        <p>A short sale can protect your credit and your peace of mind. Learn the first steps to take before you call your lender.</p>
        <a class="more" href="#">Read More</a>
      </div>
    </article>
    <article class="post">
      <div class="post-img two" role="img" aria-label="Suburban family home with front lawn"><span class="tag">Market</span></div>
      <div>
        <h3>Contantey sit amet lorme sit dol</h3>
        <p class="meta">Admin · 5 Comments</p>
        <p>Agents share how clear paperwork and early talks with lien holders help every short sale close faster and smoother.</p>
        <a class="more" href="#">Read More</a>
      </div>
    </article>
  </div>
</section>

<section class="connect">
  <div class="connect-col">
    <div class="connect-head"><p class="small">Our Clients</p><p class="big">Testimonials</p></div>
    <div class="testimonial">
      <div class="avatar" role="img" aria-label="Client portrait"></div>
      <h4>Marla Quent</h4>
      <p class="role">Homeowner, Ohio</p>
      <blockquote>“They handled every call with our lender and kept us informed each week. We sold the house without stress and finally had room to start again.”</blockquote>
      <div class="dots"><span class="on"></span><span></span><span></span></div>
    </div>
  </div>
  <div class="connect-col">
    <div class="connect-head"><p class="small">Contact Us</p><p class="big">For More Information</p></div>
    <form class="contact-form">
      <div class="row"><div class="field">First Name</div><div class="field">Last Name</div></div>
      <div class="row"><div class="field">Email</div><div class="field">Phone</div></div>
      <div class="row"><div class="field msg">Message</div></div>
      <a class="btn" href="#">SUBMIT</a>
    </form>
  </div>
</section>

<footer class="site-footer">
  <nav class="foot-nav">
    <a class="active" href="#">Home</a><a href="#">About Us</a><a href="#">Services</a><a href="#">Properties</a><a href="#">Advice</a><a href="#">Blog</a><a href="#">Contact Us</a>
  </nav>
  <div class="social"><span></span><span></span><span></span><span></span></div>
  <p class="copy">Copyright © brightgatehomes.example</p>
  <span class="to-top">TOP</span>
</footer>

</body>
</html>
```